Enduring Hurricane Rosalind: Cover Design Project

Designers! 28 October 2025 was a day I will never forget. I am writing a book about my experience.

Enduring Rosalind is a gripping, first-person account of surviving the first-ever Category 5 hurricane to directly strike Jamaica. The narrative follows a father, his girlfriend, and their 20-month-old son as they endure three weeks of total infrastructure collapse—no water, power, or cellular service.

Unlike a typical disaster memoir, this book focuses on modern preparedness and self-reliance. It details the strategic use of solar power (Voltaro units), satellite technology (Skyvane), and the psychological resilience required to protect a family while the island’s landscape is literally rewritten by 160mph winds. It is a story of survival, the "inconvenience of convenience" regarding elderly parents, and the hard lessons learned about government and infrastructure fragility.
Updates

Designers, thank you all for the amazing designs. You are making it a tough decision to pick the best one! I appreciate you all.

Gerald

Target Market(s)

Residents of hurricane-prone regions (Caribbean, Gulf Coast, etc.). "Preppers" and survivalists interested in off-grid technology. Parents interested in family protection and emergency planning. Travelers and expats living in the tropics.

Industry/Entity Type

I will be requesting a file for an e-book, paperback, hardcover, and listenly. High-resolution front cover (for eBook). Full wrap (Front, Spine, and Back) for print (Brindle BPS/FolioCrest specs). Source files (AI, PSD, or EPS). I would like a jpg mock-up for marketing purposes once finalized.

Font styles to use
Serif

Requirements
Must have
• Tone: Intense, authentic, resilient, and sophisticated. It should feel like a "Journalistic Memoir" meets a "Survival Guide." Visual Style: High contrast. I want to see a juxtaposition between the chaos of nature (darkness, storm, destroyed palms) and the glow of human resilience (light from a solar generator, a safe room, or a glowing window). Color Palette: Deep storm grays, teals, and blacks, contrasted with "survival orange" (evoking Voltaro/preparedness gear) or a warm, safe yellow light. Main Title: Enduring Rosalind (Must be bold, commanding, and easily readable in thumbnail size). Subtitle: Resilience, Solar Power, and the Category 5 hurricane that Changed Jamaica (Clean, modern sans-serif). Author Name: Dr. Gerald Whitcombe
Nice to have
• The Storm’s Power: Imagery of the catastrophic wind or the "270-degree turn" on a satellite map. Massive, uprooted tropical trees (the "toy trees" mentioned in the book). Modern Survival Tech: A subtle nod to solar panels or a portable power station. The concept of "Light in the Darkness." The Human Element: A silhouette of a family, or a small, poignant item like a child’s toy (representing the author's son, Tobin) amidst the debris. Jamaican Identity: Subtle Caribbean cues—the shape of the island, tropical flora (even if damaged), or colors that hint at the Jamaican flag without being cliché. The "Sanctuary": The idea of an interior "safe room" or closet being the last line of defense.

```html
<!DOCTYPE html>
<html lang="en">
<head>
<meta charset="UTF-8">
<title>Enduring Rosalind — Book Cover</title>
<link rel="stylesheet" href="https://fonts.googleapis.com/css2?family=Playfair+Display:wght@400;700;900&family=Lato:wght@400&display=swap">
<style>
  :root {
    --storm-sky: #2e3a44;
    --storm-deep: #1a2128;
    --storm-sea: #3b4a50;
    --ground: #1e1a16;
    --glow: #e8902e;
    --glow-soft: rgba(232, 144, 46, 0.55);
    --ink: #000000;
    --title-white: #ffffff;
    --title-shade: #c9cacc;
    --text-white: #f4f4f4;
  }
  html, body {
    margin: 0;
    padding: 0;
    overflow: hidden;
    background: var(--ink);
  }
  .cover {
    position: relative;
    width: 800px;
    height: 1200px;
    overflow: hidden;
    background: var(--ink);
  }
  .cover-scene {
    position: absolute;
    inset: 0 0 auto 0;
    height: 1020px;
    background:
      radial-gradient(ellipse 150px 120px at 440px 370px, var(--glow-soft), transparent 70%),
      radial-gradient(ellipse 260px 200px at 430px 420px, rgba(120, 70, 30, 0.35), transparent 75%),
      linear-gradient(180deg, var(--storm-sky) 0%, var(--storm-deep) 25%, var(--storm-sea) 33%, #2a2a26 45%, var(--ground) 62%, #0d0c0b 85%, var(--ink) 100%);
  }
  .cover-title {
    position: absolute;
    left: 0;
    right: 0;
    top: 655px;
    margin: 0;
    text-align: center;
    font-family: "Playfair Display", serif;
    color: var(--title-white);
    background: linear-gradient(180deg, var(--title-white) 45%, var(--title-shade) 100%);
    -webkit-background-clip: text;
    background-clip: text;
    -webkit-text-fill-color: transparent;
    line-height: 1;
  }
  .cover-title__first {
    display: block;
    font-weight: 900;
    font-size: 104px;
    letter-spacing: 2px;
  }
  .cover-title__second {
    display: block;
    margin-top: 8px;
    font-weight: 400;
    font-size: 92px;
    letter-spacing: 22px;
    padding-left: 22px;
  }
  .cover-subtitle {
    position: absolute;
    left: 0;
    right: 0;
    top: 878px;
    margin: 0;
    text-align: center;
    font-family: "Lato", sans-serif;
    font-weight: 400;
    font-size: 25px;
    line-height: 29px;
    letter-spacing: 0.5px;
    text-transform: uppercase;
    color: var(--text-white);
  }
  .cover-author {
    position: absolute;
    left: 0;
    right: 0;
    top: 1085px;
    margin: 0;
    text-align: center;
    font-family: "Playfair Display", serif;
    font-weight: 900;
    font-size: 46px;
    letter-spacing: 1px;
    text-transform: uppercase;
    color: var(--text-white);
  }
</style>
</head>
<body>
  <main class="cover">
    <div class="cover-scene" role="img" aria-label="Night storm scene: a battered wooden hut glowing with warm lantern light beside a small solar panel, surrounded by bent and uprooted palm trees, crashing waves and flooded debris under heavy rain"></div>

    <h1 class="cover-title">
      <span class="cover-title__first">ENDURING</span>
      <span class="cover-title__second">ROSALIND</span>
    </h1>

    <p class="cover-subtitle">Resilience, Solar Power, and<br>the Category 5 Hurricane that<br>Changed Jamaica</p>

    <p class="cover-author">Dr. Gerald Whitcombe</p>
  </main>
</body>
</html>
```